Stationary for ultrasound imaging company
Business card, letter head, statonary envelope, fax cover sheet
Silver-Fern
Lino Varsek
Account Executive
20947 Marlow Pine Lane
Houston, TX 77095
linovarsek@postmeadow.com
at www.brisolavent.com
This is the logo for the company.

```html
<!DOCTYPE html>
<html lang="en">
<head>
<meta charset="utf-8">
<title>Silver-Fern Stationery</title>
<link href="https://fonts.googleapis.com/css2?family=Open+Sans:wght@400;600;700&display=swap" rel="stylesheet">
<style>
:root{
  --blue:#3aa3dc;
  --blue-dark:#2489c2;
  --grey:#8d9094;
  --grey-light:#c9cbce;
  --paper:#ffffff;
  --ink:#5a5d61;
  --backdrop:#ececec;
}
*{margin:0;padding:0;box-sizing:border-box}
html,body{width:1200px;height:466px;overflow:hidden;background:var(--backdrop);font-family:"Open Sans",Arial,sans-serif;color:var(--ink)}
.canvas{position:relative;width:1200px;height:466px}
.sheet{position:absolute;background:var(--paper);box-shadow:0 2px 6px rgba(0,0,0,.18);overflow:hidden}
.sheet svg.swoosh{position:absolute;left:0;width:100%}
.brand{position:absolute;display:flex;align-items:center;gap:4px;font-weight:700;color:var(--blue);white-space:nowrap}
.brand .mark{background:var(--blue);display:block}
.contact{position:absolute;font-size:4px;line-height:6px;color:var(--ink);white-space:nowrap}
/* business cards */
.card-front{left:12px;top:312px;width:84px;height:48px}
.card-front .brand{left:6px;top:5px;font-size:6.5px;gap:3px}
.card-front .brand .mark{width:6px;height:6px}
.card-front .contact{left:6px;top:15px;font-size:3px;line-height:3.7px}
.card-front .contact .name{font-weight:700;color:var(--blue)}
.card-back{left:12px;top:384px;width:84px;height:48px;background:var(--blue)}
.card-back .tile{position:absolute;left:34px;top:16px;width:16px;height:16px;background:var(--paper)}
/* letterheads */
.letter-one{left:259px;top:24px;width:197px;height:252px}
.letter-two{left:480px;top:24px;width:199px;height:252px}
.letter-one .brand{left:12px;top:14px;font-size:11px}
.letter-one .brand .mark{width:10px;height:10px}
.letter-one .contact{left:128px;top:12px}
.letter-two .brand{left:14px;top:30px;font-size:11px}
.letter-two .brand .mark{width:10px;height:10px}
.letter-two .watermark{position:absolute;left:69px;top:92px;width:60px;height:60px;background:var(--blue);opacity:.1}
.letter-two .footer{position:absolute;left:0;right:0;bottom:12px;text-align:center;font-size:3.6px;color:var(--ink);white-space:nowrap}
/* envelopes */
.envelope-back{left:710px;width:226px;height:76px}
.envelope-back svg{position:absolute;inset:0}
.env-blue{top:29px}
.env-grey{top:112px}
.env-white{top:195px}
.envelope-back .seal{position:absolute;left:107px;top:26px;width:12px;height:12px;background:var(--paper)}
.env-white .seal{background:var(--blue)}
.envelope-front{left:710px;top:282px;width:226px;height:106px}
.envelope-front .brand{left:10px;top:10px;font-size:11px}
.envelope-front .brand .mark{width:10px;height:10px}
.envelope-front .contact{left:10px;top:28px}
</style>
</head>
<body>
<main class="canvas">

  <section class="sheet card-front" aria-label="Business card front">
    <div class="brand"><span class="mark"></span>Silver-Fern</div>
    <div class="contact">
      <div class="name">Lino Varsek</div>
      <div>Account Executive</div>
      <div>20947 Marlow Pine Lane, Houston, TX 77095</div>
      <div>linovarsek@postmeadow.com</div>
      <div>www.brisolavent.com</div>
    </div>
    <svg class="swoosh" style="bottom:0;height:12px" viewBox="0 0 84 12" preserveAspectRatio="none">
      <path d="M0 6 C30 12 55 1 84 3 L84 12 L0 12Z" fill="var(--grey)"/>
      <path d="M0 8 C30 14 55 4 84 6 L84 12 L0 12Z" fill="var(--blue)"/>
    </svg>
  </section>

  <section class="sheet card-back" aria-label="Business card back">
    <span class="tile"></span>
  </section>

  <section class="sheet letter-one" aria-label="Letterhead option one">
    <div class="brand"><span class="mark"></span>Silver-Fern</div>
    <div class="contact">
      <div>20947 Marlow Pine Lane</div>
      <div>Houston, TX 77095</div>
      <div>linovarsek@postmeadow.com</div>
      <div>www.brisolavent.com</div>
    </div>
    <svg class="swoosh" style="bottom:0;height:48px" viewBox="0 0 197 48" preserveAspectRatio="none">
      <path d="M0 14 C70 44 130 4 197 18 L197 48 L0 48Z" fill="var(--grey)"/>
      <path d="M0 24 C70 50 130 14 197 26 L197 48 L0 48Z" fill="var(--blue)"/>
      <path d="M0 32 C70 54 130 24 197 34 L197 48 L0 48Z" fill="var(--blue-dark)" opacity=".35"/>
    </svg>
  </section>

  <section class="sheet letter-two" aria-label="Letterhead option two">
    <svg class="swoosh" style="top:0;height:30px" viewBox="0 0 199 30" preserveAspectRatio="none">
      <path d="M0 0 L199 0 L199 26 C140 4 80 6 0 14Z" fill="var(--grey)"/>
      <path d="M0 0 L199 0 L199 16 C140 0 80 2 0 8Z" fill="var(--blue)"/>
    </svg>
    <div class="brand"><span class="mark"></span>Silver-Fern</div>
    <span class="watermark"></span>
    <div class="footer">20947 Marlow Pine Lane, Houston, TX 77095 · linovarsek@postmeadow.com · www.brisolavent.com</div>
  </section>

  <section class="sheet envelope-back env-blue" aria-label="Envelope back, blue flap">
    <svg viewBox="0 0 226 76" preserveAspectRatio="none">
      <path d="M0 0 L226 0 L226 10 L113 50 L0 10Z" fill="var(--blue)"/>
      <path d="M0 76 L113 40 L226 76" fill="none" stroke="var(--grey-light)" stroke-width=".6"/>
    </svg>
    <span class="seal"></span>
  </section>

  <section class="sheet envelope-back env-grey" aria-label="Envelope back, grey flap">
    <svg viewBox="0 0 226 76" preserveAspectRatio="none">
      <path d="M0 0 L226 0 L226 10 L113 50 L0 10Z" fill="var(--grey)"/>
      <path d="M0 76 L113 40 L226 76" fill="none" stroke="var(--grey-light)" stroke-width=".6"/>
    </svg>
    <span class="seal"></span>
  </section>

  <section class="sheet envelope-back env-white" aria-label="Envelope back, white flap">
    <svg viewBox="0 0 226 76" preserveAspectRatio="none">
      <path d="M0 0 L226 0 L226 10 L113 50 L0 10Z" fill="#f6f6f6" stroke="var(--grey-light)" stroke-width=".6"/>
      <path d="M0 76 L113 40 L226 76" fill="none" stroke="var(--grey-light)" stroke-width=".6"/>
    </svg>
    <span class="seal"></span>
  </section>

  <section class="sheet envelope-front" aria-label="Envelope front">
    <div class="brand"><span class="mark"></span>Silver-Fern</div>
    <div class="contact">
      <div>20947 Marlow Pine Lane</div>
      <div>Houston, TX 77095</div>
    </div>
    <svg class="swoosh" style="bottom:0;height:30px" viewBox="0 0 226 30" preserveAspectRatio="none">
      <path d="M0 8 C80 30 150 2 226 12 L226 30 L0 30Z" fill="var(--grey)"/>
      <path d="M0 16 C80 34 150 10 226 18 L226 30 L0 30Z" fill="var(--blue)"/>
    </svg>
  </section>

</main>
</body>
</html>
```